Postcard Design for Thank Yous

I am a Voice Actor and want to send personal thank you cards or postcards to clients after recording sessions. the basic concept is front art that simply has background art & my logo (sample below but wrong size), and the other side would be space for mailing address as well as a small version of my logo and contact info and of course plenty of blank space for me to write a personal message. I am open to your opinion as to whether a postcard, or a card and mailing envelope makes more sense. (I am also including the back of business card as example of contact listing, but one number will not be included and I might want to change other verbiage). Thank you! -Neil

```html
<!DOCTYPE html>
<html lang="en">
<head>
<meta charset="utf-8">
<title>Thank You Postcard – Front and Back</title>
<link rel="stylesheet" href="https://fonts.googleapis.com/css2?family=Open+Sans:wght@600;700&display=swap">
<style>
  :root {
    --page: #d9d9d9;
    --ink-black: #0c0c0c;
    --photo-dark: #2a2a2a;
    --photo-mid: #6b6b68;
    --photo-light: #a3a39f;
    --accent-red: #e3141b;
    --paper: #ffffff;
    --text-light: #ffffff;
    --rule-grey: #9a9a9a;
    --stamp-line: #111111;
  }
  * { box-sizing: border-box; margin: 0; padding: 0; }
  html, body { width: 1200px; height: 505px; overflow: hidden; }
  body {
    background: var(--page);
    font-family: "Open Sans", Arial, sans-serif;
    position: relative;
  }

  /* Contact card (front) */
  .contact-card {
    position: absolute; left: 40px; top: 55px;
    width: 520px; height: 395px;
    background: var(--ink-black);
    overflow: hidden;
  }
  .contact-card .table-photo {
    position: absolute; inset: 0;
    background: radial-gradient(ellipse at 45% 50%, var(--photo-light) 0%, var(--photo-mid) 45%, var(--photo-dark) 75%, var(--ink-black) 100%);
  }
  .contact-card .red-arcs { position: absolute; inset: 0; }
  .brand-mark {
    position: absolute; display: flex; align-items: center; gap: 6px;
    color: var(--text-light); font-weight: 700; font-size: 11px; letter-spacing: .02em;
  }
  .brand-mark .brand-square { width: 26px; height: 26px; background: var(--accent-red); }
  .contact-card .brand-mark { left: 18px; top: 18px; }
  .contact-details {
    position: absolute; left: 70px; top: 118px; width: 380px;
    color: var(--text-light); text-align: center; font-weight: 600;
    text-shadow: 0 1px 3px rgba(0,0,0,.6);
  }
  .contact-details .name-line {
    font-size: 21px; font-weight: 700;
    border-bottom: 2px solid var(--text-light); padding-bottom: 2px;
  }
  .contact-details .detail { font-size: 19px; line-height: 27px; }
  .contact-details .website { margin-top: 2px; }
  .contact-card .closing-rule {
    position: absolute; left: 100px; top: 318px; width: 320px; height: 2px;
    background: var(--text-light);
  }
  .contact-card .closing {
    position: absolute; left: 0; right: 0; top: 328px;
    text-align: center; color: var(--text-light); font-size: 24px; font-weight: 700;
    text-shadow: 0 1px 3px rgba(0,0,0,.6);
  }

  /* Mailing card (back) */
  .mailing-card {
    position: absolute; left: 600px; top: 45px;
    width: 560px; height: 415px;
    background: var(--paper);
    overflow: hidden;
  }
  .mailing-card .table-photo {
    position: absolute; left: 0; top: 0; width: 260px; height: 100%;
    background: radial-gradient(ellipse at 60% 55%, var(--photo-light) 0%, var(--photo-mid) 50%, var(--photo-dark) 100%);
  }
  .mailing-card .brand-mark { left: 14px; top: 18px; }
  .mailing-card .closing {
    position: absolute; left: 16px; bottom: 52px;
    color: var(--text-light); font-size: 24px; font-weight: 700;
    text-shadow: 0 1px 3px rgba(0,0,0,.6);
  }
  .stamp-box {
    position: absolute; right: 48px; top: 14px;
    width: 110px; height: 110px; border: 2px solid var(--stamp-line);
  }
  .address-lines {
    position: absolute; left: 298px; top: 205px; width: 210px;
    display: flex; flex-direction: column; gap: 36px;
  }
  .address-lines span { display: block; height: 1px; background: var(--rule-grey); }
</style>
</head>
<body>

  <section class="contact-card">
    <div class="table-photo" role="img" aria-label="Black and white photo of a card table with playing cards and stacks of poker chips"></div>
    <svg class="red-arcs" width="520" height="395" viewBox="0 0 520 395" aria-hidden="true">
      <path d="M0 205 Q70 40 255 0 L262 0 Q85 50 8 200 Z" fill="var(--accent-red)"/>
      <path d="M520 215 Q470 360 330 395 L345 395 Q490 360 520 235 Z" fill="var(--accent-red)"/>
    </svg>
    <div class="brand-mark"><span class="brand-square"></span><span>Halvorsen Voice</span></div>
    <div class="contact-details">
      <div class="name-line">Neil Halvorsen - Voice Actor</div>
      <div class="detail website">www.neilhalvorsenvoice.com</div>
      <div class="detail">Office:513.555.0142</div>
      <div class="detail">cell:513.555.0187</div>
      <div class="detail">Studio Phone:513.555.0163</div>
    </div>
    <div class="closing-rule"></div>
    <div class="closing">Thank you! -Neil</div>
  </section>

  <section class="mailing-card">
    <div class="table-photo" role="img" aria-label="Black and white photo of playing cards and poker chips on a card table"></div>
    <div class="brand-mark"><span class="brand-square"></span><span>Halvorsen Voice</span></div>
    <div class="closing">Thank you! -Neil</div>
    <div class="stamp-box"></div>
    <div class="address-lines"><span></span><span></span><span></span></div>
  </section>

</body>
</html>
```